one stop shop
concierge service
Project: one stop shop
one stop shop - Administrative Services
Creative Brief
Administrative Services
www.tidewellhome.example
new company. taking care of entire home and house needs of those living in Marin County, California. housecleaning, babysitting, elder care, home repairs, groceries and errand, lawn maintenance catering, interior design, customer makes one call to us and we do all the leg work to ensure their needs are met. We have full list of contractors in all areas so quick turn around can be expected. we are a concierge service
no flash - clean look.
left side
page one is the description of what we do and who we are. Page two can be People - day care, elder care, errands page three can be Home - interior design, home maintenance, house cleaning, carpets cleaned, windows washed. Page four Events - day sails, catering, bike rentals
tolvark tolvark
I want to have one page to portray the personal needs such as babysitting or elder care. One page to portray home care such as house cleaning, carpet cleaning, windows washed light maintenance and interior design. One page for events such as bike rentals, catering, sailing, does this help . I have a logo - just need to figure out how to load it to you
i'd like the front page to show home care, personal care, and event like sailing, catering. full concierge care for all of your at home needs.
pibble4 pibble4
Hi , Can you please provide the Company Logo for the website. Thanks

```html
<!DOCTYPE html>
<html lang="en">
<head>
<meta charset="utf-8">
<title>Tidewell Home – Concierge Service</title>
<link href="https://fonts.googleapis.com/css2?family=Arimo:ital,wght@0,400;0,700;1,400&family=Oswald:wght@300;400&family=Open+Sans:wght@600;700&family=Roboto:wght@400;500&family=Tinos&display=swap" rel="stylesheet">
<style>
:root{
  --blue:#2a3590;
  --blue-dark:#1f2a78;
  --green:#8cc63f;
  --green-dark:#74ad2b;
  --header-bg:#eef0e4;
  --grey-band:#eeeeee;
  --text:#222;
  --muted:#555;
  --white:#fff;
}
*{margin:0;padding:0;box-sizing:border-box}
html,body{width:960px;height:1200px;overflow:hidden}
body{position:relative;background:var(--white);font-family:"Arimo",Arial,sans-serif;color:var(--text)}
.abs{position:absolute}

/* header */
.site-header{left:0;top:0;width:960px;height:105px;background:var(--header-bg)}
.brand{left:122px;top:64px;font:700 22px "Arimo",Arial,sans-serif;color:var(--blue);display:flex;align-items:center;gap:8px}
.brand-dot{width:14px;height:14px;border-radius:50%;background:var(--green)}
.hotline{left:678px;top:8px;display:flex;gap:6px}
.hotline-icon{width:25px;height:25px;border-radius:50%;background:var(--green);margin-top:7px;display:flex;align-items:center;justify-content:center}
.hotline-label{font:400 16px/1 "Oswald",sans-serif;color:#333}
.hotline-number{font:300 16px/1.3 "Oswald",sans-serif;color:var(--blue)}
.main-nav{left:333px;top:67px;display:flex;gap:4px}
.main-nav a{display:block;height:20px;padding:0 7px;border:1px solid var(--green);border-radius:3px;background:#fafbf4;font:600 10.5px/18px "Open Sans",sans-serif;color:#333;text-decoration:none;letter-spacing:.2px}
.main-nav a.is-active{background:var(--blue);border-color:var(--blue-dark);color:var(--white)}

/* hero */
.hero{left:0;top:105px;width:960px;height:310px;background:linear-gradient(180deg,#c9d8e6 0%,#9ba5ad 40%,#7d8a70 70%,#4f8a2a 100%)}
.hero-dots{left:800px;top:398px;display:flex;gap:4px}
.hero-dots span{width:9px;height:9px;border-radius:50%;background:#ccc;border:1px solid #fff}
.hero-dots span.is-current{background:#f26b21}
.ribbon{left:0;top:370px}

/* service cards */
.service{width:215px}
.service-photo{height:122px;border:3px solid var(--green);background:linear-gradient(135deg,#e8d9c8,#b9a38d)}
.service-label{position:absolute;left:-10px;top:85px;height:24px;padding:0 30px 0 16px;background:var(--blue);color:var(--white);font:400 15px/24px "Tinos",serif;clip-path:polygon(0 0,100% 0,calc(100% - 10px) 100%,0 100%)}
.service-list{list-style:none;margin:9px 0 0 8px}
.service-list li{font:500 10px/19px "Roboto",sans-serif;color:#333;letter-spacing:.3px;padding-left:12px;position:relative}
.service-list li::before{content:"";position:absolute;left:0;top:7px;width:5px;height:5px;border-top:1.5px solid var(--green);border-right:1.5px solid var(--green);transform:rotate(45deg)}
.read-more{display:inline-block;margin:11px 0 0 1px;font:700 9px "Arimo",sans-serif;color:var(--blue);text-decoration:none}
.read-more-swoosh{display:block;margin-top:1px}

/* about */
.about-band{left:0;top:705px;width:960px;height:205px;background:linear-gradient(180deg,var(--grey-band),#fafafa)}
.about-title{left:114px;top:713px;display:flex;gap:10px;align-items:flex-start}
.about-title .mark{width:14px;height:14px;background:var(--green);margin-top:12px;border-radius:2px}
.about-title h2{font:400 19px/1 "Tinos",serif;color:#333;padding-left:50px}
.about-title h3{font:700 14px/1.2 "Arimo",sans-serif;color:var(--blue);padding-left:48px}
.about-rule{left:113px;top:757px;width:484px;height:5px;background:repeating-linear-gradient(135deg,#ccc 0 1px,transparent 1px 3px)}
.about-text{left:114px;top:770px;width:483px;font:400 8.6px/14.3px "Arimo",sans-serif;color:#222;text-align:justify}
.call-bar{left:113px;top:861px;width:476px;height:30px;background:#f2f2f2;border:1px solid #ddd;display:flex;align-items:center;padding-left:6px}
.call-bar strong{font:700 14px "Arimo",sans-serif;color:var(--blue)}
.call-bar small{font:700 9.5px "Arimo",sans-serif;color:#555;margin-left:16px}
.call-bar .call-number{font:400 15px "Arimo",sans-serif;color:var(--green);margin-left:6px}
.call-bar svg{margin-left:20px}

/* quick contact */
.contact-title{left:613px;top:728px;font:400 20px "Tinos",serif;color:var(--blue)}
.contact-form{left:611px;top:755px;width:236px;height:136px;border:1px solid #b8dc8e;border-radius:0 0 12px 0;background:var(--white)}
.field{position:absolute;left:14px;width:210px;border:1px solid #bbb;border-radius:2px;background:#fff;font:400 9.5px "Arimo",sans-serif;color:#333;padding:4px 7px}
.submit{position:absolute;left:14px;top:108px;width:52px;height:18px;background:var(--blue);color:var(--white);font:700 9px/18px "Arimo",sans-serif;text-align:center;border-radius:2px;letter-spacing:.5px}

/* testimonial */
.testimonial{left:120px;top:924px;width:718px;height:112px;border:2px solid #ddd;border-radius:6px;background:var(--white)}
.testimonial-tail{left:150px;top:1034px}
.testimonial-photo{left:127px;top:932px;width:176px;height:94px;background:linear-gradient(135deg,#9fc56a,#d9b08a 60%,#7fa84a)}
.quote-mark{left:314px;top:925px;font:400 48px/1 "Tinos",serif;color:#ccc}
.quote-text{left:349px;top:938px;width:460px;font:italic 400 9.3px/15.5px "Arimo",sans-serif;color:#222}
.quote-author{left:351px;top:1007px;font:700 9.5px "Arimo",sans-serif;color:var(--blue)}
.quote-arrows{left:795px;top:1010px}

/* footer */
.site-footer{left:0;top:1063px;width:960px;height:137px;background:var(--green)}
.footer-heading{font:400 16px "Tinos",serif;color:#111}
.footer-links{list-style:none}
.footer-links li{font:400 9.5px/19.5px "Arimo",sans-serif;color:var(--white);padding-left:12px;position:relative}
.footer-links li::before{content:"›";position:absolute;left:0;top:-1px;font-size:10px}
.footer-divider{width:1px;height:120px;background:rgba(0,0,0,.12);box-shadow:1px 0 0 rgba(255,255,255,.3)}
.footer-map{left:310px;top:1104px;width:156px;height:74px;border:3px solid #666;background:linear-gradient(135deg,#e6e7de,#cfd6c3)}
.contact-line{display:flex;align-items:center;gap:8px;font:400 8.6px "Arimo",sans-serif;color:var(--white);height:23px}
.contact-line b{font-weight:700}
.socials{left:501px;top:1173px;display:flex;gap:4px}
.socials span{width:13px;height:13px;border-radius:3px;background:var(--white)}
.footer-brand{left:663px;top:1105px;width:180px;text-align:center;font:700 20px "Arimo",sans-serif;color:var(--white)}
.copyright{left:663px;top:1153px;width:180px;text-align:center;font:400 8.8px "Arimo",sans-serif;color:var(--white)}
</style>
</head>
<body>

<header class="site-header abs"></header>
<div class="brand abs"><span class="brand-dot"></span>Tidewell Home</div>

<div class="hotline abs">
  <div class="hotline-icon">
    <svg width="13" height="13" viewBox="0 0 24 24"><path fill="#fff" d="M6.6 10.8a15 15 0 0 0 6.6 6.6l2.2-2.2c.3-.3.7-.4 1-.2 1.1.4 2.3.6 3.6.6.6 0 1 .4 1 1V20c0 .6-.4 1-1 1A17 17 0 0 1 3 4c0-.6.4-1 1-1h3.5c.6 0 1 .4 1 1 0 1.3.2 2.5.6 3.6.1.3 0 .7-.2 1z"/></svg>
  </div>
  <div>
    <div class="hotline-label">For Concierge service</div>
    <div class="hotline-number">(555) 010-0199</div>
  </div>
</div>

<nav class="main-nav abs">
  <a href="#" class="is-active">HOME</a>
  <a href="#">ABOUT US</a>
  <a href="#">HOME CARE</a>
  <a href="#">PERSONAL CARE</a>
  <a href="#">EVENTS/ACTIVITIES</a>
  <a href="#">CONTACT US</a>
</nav>

<section class="hero abs" role="img" aria-label="Smiling multi-generation family standing in front of a large grey suburban house with a green lawn"></section>
<div class="hero-dots abs"><span class="is-current"></span><span></span><span></span><span></span></div>

<svg class="ribbon abs" width="960" height="90" viewBox="0 370 960 90">
  <path d="M112 415 Q330 378 560 384 Q680 388 722 402 L846 448 Q760 422 600 420 Q400 420 232 452 Q160 444 112 415 Z" fill="var(--green)"/>
  <path id="ribbon-curve" d="M238 446 Q470 392 712 410" fill="none"/>
  <text font-family="Tinos, serif" font-size="18" fill="#fff" letter-spacing=".4"><textPath href="#ribbon-curve">ONE STOP SHOP FOR ALL YOUR CONCIERGE NEEDS</textPath></text>
</svg>

<article class="service abs" style="left:122px;top:474px">
  <div class="service-photo" role="img" aria-label="Younger woman embracing an elderly woman"></div>
  <div class="service-label">PERSONAL NEEDS</div>
  <ul class="service-list"><li>Day Care</li><li>Elder Care</li><li>Errands</li></ul>
  <a class="read-more" href="#">Read More »<svg class="read-more-swoosh" width="62" height="6" viewBox="0 0 62 6"><path d="M0 1 Q30 7 62 2 Q30 4 0 1Z" fill="var(--green)" stroke="var(--green)" stroke-width="1.5"/></svg></a>
</article>

<article class="service abs" style="left:369px;top:474px">
  <div class="service-photo" role="img" aria-label="Couple looking at paint colour swatches for a room"></div>
  <div class="service-label">HOME CARE SERVICES</div>
  <ul class="service-list"><li>Interior Design</li><li>Home Maintenance</li><li>House Cleaning</li></ul>
  <a class="read-more" href="#">Read More »<svg class="read-more-swoosh" width="62" height="6" viewBox="0 0 62 6"><path d="M0 1 Q30 7 62 2 Q30 4 0 1Z" fill="var(--green)" stroke="var(--green)" stroke-width="1.5"/></svg></a>
</article>

<article class="service abs" style="left:617px;top:474px">
  <div class="service-photo" role="img" aria-label="Smiling caterer in a black apron"></div>
  <div class="service-label">EVENTS/ACTIVITIES</div>
  <ul class="service-list"><li>Day Sails</li><li>Catering</li><li>Bike Rentals</li></ul>
  <a class="read-more" href="#">Read More »<svg class="read-more-swoosh" width="62" height="6" viewBox="0 0 62 6"><path d="M0 1 Q30 7 62 2 Q30 4 0 1Z" fill="var(--green)" stroke="var(--green)" stroke-width="1.5"/></svg></a>
</article>

<section class="about-band abs"></section>
<div class="about-title abs">
  <div>
    <h2>About</h2>
    <h3>Tidewell Home</h3>
  </div>
</div>
<div class="about-rule abs"></div>
<p class="about-text abs">Lorem ipsum dolor sit amet, consectetuer adipiscing elit, sed diam nonummy nibh euismod tincidunt ut laoree dolore magna aliquam erat volutpat. Ut wisi enim ad minim veniam, quis nostrud exerci tation ullamco suscipit lobortis nisl ut aliquip ex ea commodo consequat. Duis autem vel eum iriure dolor in hendreri vulputate velit esse mol consequat, vel illum dolore eu feugiat nulla facilisis at vero eros et accumsan et iusto dignissim qui blandit praesent luptatum zzril delenit augue duis dolore te feugait nulla facilisi.Duis autem vel eum iriure dolor in hendrerit in vulputate velit esse molestie consequat, vel illum dolore eu feugiat nulla facilisis at vero eros et accumsa.</p>
<div class="call-bar abs">
  <strong>We are a concierge service</strong>
  <small>Makes one call to us</small>
  <svg width="18" height="18" viewBox="0 0 24 24"><path fill="#333" d="M6.6 10.8a15 15 0 0 0 6.6 6.6l2.2-2.2c.3-.3.7-.4 1-.2 1.1.4 2.3.6 3.6.6.6 0 1 .4 1 1V20c0 .6-.4 1-1 1A17 17 0 0 1 3 4c0-.6.4-1 1-1h3.5c.6 0 1 .4 1 1 0 1.3.2 2.5.6 3.6.1.3 0 .7-.2 1z"/></svg>
  <span class="call-number">(555)010-0199</span>
</div>

<h2 class="contact-title abs">Quick Contact</h2>
<form class="contact-form abs">
  <div class="field" style="top:8px;height:22px">Name</div>
  <div class="field" style="top:35px;height:22px">Email</div>
  <div class="field" style="top:62px;height:41px">Message</div>
  <div class="submit">SUBMIT</div>
</form>

<section class="testimonial abs"></section>
<svg class="testimonial-tail abs" width="20" height="14" viewBox="0 0 20 14"><path d="M1 0 L17 0 L16 13 Z" fill="#fff" stroke="#ddd" stroke-width="2"/><path d="M2 0 L16 0" stroke="#fff" stroke-width="3"/></svg>
<div class="testimonial-photo abs" role="img" aria-label="Happy family of four posing outdoors"></div>
<div class="quote-mark abs">“</div>
<p class="quote-text abs">Lorem ipsum dolor sit amet, consectetuer adipiscing elit, sed diam nonummy nibh euismod tincidunt ut laoree dolore magna aliquam erat volutpat. Ut wisi enim ad minim veniam, quis nostrud exerci tation ullamco suscipit lobortis nisl ut aliquip ex ea commodo consequat. Duis autem vel eum iriure dolor in hendreri vulputate velit esse mol consequat, vel illum dolore eu</p>
<div class="quote-author abs">- Alder Family, City</div>
<svg class="quote-arrows abs" width="24" height="12" viewBox="0 0 24 12"><path d="M7 1 L2 6 L7 11" fill="none" stroke="#444" stroke-width="2"/><path d="M17 1 L22 6 L17 11" fill="none" stroke="#444" stroke-width="2"/></svg>

<footer class="site-footer abs"></footer>
<h4 class="footer-heading abs" style="left:114px;top:1075px">Quick Links</h4>
<ul class="footer-links abs" style="left:115px;top:1100px"><li>Home</li><li>About Us</li><li>Home Care</li></ul>
<ul class="footer-links abs" style="left:205px;top:1100px"><li>Personal Care</li><li>Events/Activities</li><li>Contact Us</li></ul>
<div class="footer-divider abs" style="left:295px;top:1070px"></div>
<h4 class="footer-heading abs" style="left:314px;top:1075px">Contact Us</h4>
<div class="footer-map abs" role="img" aria-label="Road map of central California with a location marker"></div>
<div class="abs" style="left:480px;top:1102px">
  <div class="contact-line"><svg width="12" height="14" viewBox="0 0 12 16"><path d="M6 0a6 6 0 0 0-6 6c0 4.5 6 10 6 10s6-5.5 6-10a6 6 0 0 0-6-6zm0 8.5A2.5 2.5 0 1 1 6 3.5a2.5 2.5 0 0 1 0 5z" fill="#fff"/></svg>Harbor Point, CA 94900 PO Box 2210</div>
  <div class="contact-line"><svg width="13" height="13" viewBox="0 0 24 24"><path fill="#fff" d="M6.6 10.8a15 15 0 0 0 6.6 6.6l2.2-2.2c.3-.3.7-.4 1-.2 1.1.4 2.3.6 3.6.6.6 0 1 .4 1 1V20c0 .6-.4 1-1 1A17 17 0 0 1 3 4c0-.6.4-1 1-1h3.5c.6 0 1 .4 1 1 0 1.3.2 2.5.6 3.6.1.3 0 .7-.2 1z"/></svg><span><b>Phone:</b> (555)010-0199</span></div>
  <div class="contact-line"><svg width="14" height="10" viewBox="0 0 14 10"><rect x=".5" y=".5" width="13" height="9" fill="none" stroke="#fff"/><path d="M.5 .5 L7 6 L13.5 .5" fill="none" stroke="#fff"/></svg><span><b>Mail :</b> info@tidewellhome.example</span></div>
</div>
<div class="socials abs"><span></span><span></span><span></span></div>
<div class="footer-divider abs" style="left:648px;top:1070px"></div>
<div class="footer-brand abs">Tidewell Home</div>
<div class="copyright abs">© 2013- Tidewell Home. All rights reserved.</div>

</body>
</html>
```